New modern and animated Design needed for a portal login site (Relayon Portal)

Relayon is software for market communication B2B & EAI.
We need a modern look for a Relayon Portal login site. We prefer a full size use for the background design of the login-page, with animation.
The name of the site is “Relayon Langzeitarchiv”, what should appear as text. Further there is space needed for the login name and password.
Responsive Design is required.
We have a new Relayon logo (find attached), that can be used for the animation, for example but not necessarily.
Feel free to visit our website for inspiration (colours etc.): www.vormelsysteme.de.
Updates

Reason: Can you please animate the backgraound and send links to view it.

Reason: there is aproblem with pixelforum - we acually cannot view any designs

Target Market(s)

energy sector, IT

Industry/Entity Type

Communication

Number of Pages Required

1 page

Font styles to use
Sans Serif

Colors

Designer to choose colors to be used in the design.

Requirements
Must have
• fullscreen background design (like "onepager"),
• animated (infinity), not to much action
• the only text that is needed is "Relayon Langzeitarchiv" (in front) and the login details: "Benutzername" (+ space for the username (free position)) and "Paswort" (+ space for the password (free position))
Nice to have
• maybe shades of blue, or colours, like the ones used on our website and logo (vormel systeme) or Relayon icon (files named "asset")
• animation can also be a film that starts over and over again (note: The up half of the page www.brunostafa.de is one example, which is nice to watch - but here it is not necessary to use a movie)

```html
<!DOCTYPE html>
<html lang="de">
<head>
<meta charset="utf-8">
<title>Relayon Langzeitarchiv – Login</title>
<link rel="stylesheet" href="https://fonts.googleapis.com/css2?family=Raleway:wght@400;500;600;700&display=swap">
<style>
  :root {
    --bg: #0077ae;
    --deco-dark: #0d57a8;
    --deco-light: #1a8fd0;
    --card: #ffffff;
    --ink: #1c5f97;
    --accent: #29a8e0;
    --rule: #e3e6ea;
    --btn-grey: #e6e7ea;
    --btn-blue: #0a8bd0;
    --btn-grey-ink: #2a5f95;
  }
  * { box-sizing: border-box; margin: 0; padding: 0; }
  html, body { width: 1200px; height: 687px; overflow: hidden; }
  body {
    background: var(--bg);
    font-family: "Raleway", sans-serif;
    position: relative;
  }
  .backdrop-shape {
    position: absolute;
    background: linear-gradient(135deg, var(--deco-dark), var(--deco-light));
    opacity: 0.55;
  }
  .backdrop-shape--upper { left: 335px; top: 98px; width: 290px; height: 212px; }
  .backdrop-shape--lower { left: 672px; top: 337px; width: 218px; height: 156px; }

  .login-card {
    position: absolute;
    left: 420px; top: 170px;
    width: 391px; height: 258px;
    background: var(--card);
    box-shadow: 0 14px 30px rgba(0, 40, 80, 0.28);
  }
  .brand {
    position: absolute;
    left: 29px; top: 21px;
    display: flex; align-items: center; gap: 10px;
  }
  .brand__mark {
    width: 30px; height: 30px;
    border-radius: 50%;
    background: var(--ink);
  }
  .brand__name {
    color: var(--ink);
    font-size: 11.5px; font-weight: 500;
    line-height: 11px; letter-spacing: 0.6px;
  }
  .partner {
    position: absolute;
    right: 26px; top: 24px;
    color: var(--ink);
    font-size: 12px; font-weight: 500;
    line-height: 11.5px; text-align: right;
  }
  .field {
    position: absolute;
    left: 32px; width: 325px;
    border-bottom: 1px solid var(--rule);
    padding-bottom: 9px;
  }
  .field--user { top: 82px; }
  .field--pass { top: 123px; }
  .field__label {
    color: var(--accent);
    font-size: 9.5px; font-weight: 500; letter-spacing: 0.7px;
    text-transform: uppercase;
  }
  .forgot {
    position: absolute;
    top: 167px; left: 0; width: 100%;
    text-align: center;
    color: var(--accent);
    font-size: 9px; font-weight: 500; letter-spacing: 0.8px;
    text-transform: uppercase;
    padding-left: 6px;
  }
  .actions {
    position: absolute;
    left: 0; bottom: 0; width: 100%; height: 39px;
    display: flex;
  }
  .actions__btn {
    display: flex; align-items: center;
    font-size: 9.5px; font-weight: 700; letter-spacing: 0.8px;
    text-transform: uppercase;
  }
  .actions__btn--register {
    width: 197px; background: var(--btn-grey);
    color: var(--btn-grey-ink); padding-left: 14px;
  }
  .actions__btn--login {
    flex: 1; background: var(--btn-blue);
    color: #fff; justify-content: flex-end; padding-right: 14px;
  }
</style>
</head>
<body>
  <div class="backdrop-shape backdrop-shape--upper" role="img" aria-label="Geometrische Dreiecksfläche in Blautönen"></div>
  <div class="backdrop-shape backdrop-shape--lower" role="img" aria-label="Geometrische Dreiecksfläche in Blautönen"></div>

  <main class="login-card">
    <div class="brand">
      <span class="brand__mark"></span>
      <span class="brand__name">relayon<br>langzeitarchiv</span>
    </div>
    <div class="partner">vormel<br>systeme</div>

    <div class="field field--user"><span class="field__label">Benutzername</span></div>
    <div class="field field--pass"><span class="field__label">Passwort</span></div>

    <div class="forgot">Passwort vergessen?</div>

    <div class="actions">
      <div class="actions__btn actions__btn--register">Registrieren</div>
      <div class="actions__btn actions__btn--login">Einloggen</div>
    </div>
  </main>
</body>
</html>
```